Company profile urgent

Hi, I had my designer fail to deliver and I am looking for urgent designers job. Needs to go to print tomorrow the latest. I need company profile designed and finished, I do have a start of the project but did not like the overall design as it was too simple and not something I would asking for. This needs to be a great job and we are willing to pay for the right job.

This is pretty much a folded brochure as you will see from the document that is attached. On the front side do not remove LOGO from the actual position as it must stay there for the purposes of the cover that is going over and it has a whole for the logo where it is. Also, the pages are set as it should be so do not change the order of the pages, only the design, feel and look. This is for a travel company needs to look expensive, upscale, vip and must have clean design.

Needs to be done:

.

Needs to be done:

1) Get the design more attractive and modern. Not looking for cheap but high quality material.
2) As you can see we are tryin to present 4 products in the brochure that we do and this will be a folded brochure.
3) Infographics, especially the table ''when to travel'' needs updates and more style
4) This design is very steril, we are looking for clean and modern design
5) On the front page add Company profile text somewhere and add any design on home page is welcome BUT logo must stay where is
6) Please send final print ready documents as well as editable so we can move the logo if needed as it must fit the whole on a brochure holder
7) Last page with contacts very poorly done by my designer, needs upgrade with maybe infographics for phone, email web etc... ideas welcome
8) if you need more photos at the end is link to photo bank

Ideas welcome! Again we need it fast and clean.

Photo bank:
https://files.orvenbox.example/f/q7Lm2Xa9Tz4Pb8Kd

Designes that we linked: https://layoutmarket.example/item/company-profile-square-brochure/48817203?s_rank=8
https://layoutmarket.example/item/company-profile_square/51390628?s_rank=32
https://layoutmarket.example/item/square-brochure/53704916?s_rank=52

This is our webiste so you get the feeling of the colors: www.selvotrips.example

Important: Do not change text, or change pages, everything is as it should be just needs upgradede design! Logo on the first page must stay on the position as is.

Photo bank:

Target Market(s)

We are travel supplier targeting travel agents and travel companies

Industry/Entity Type

Travel Industry

Font styles to use
Serif
Sans Serif

Requirements
Must have
• https://files.orvenbox.example/f/w3Hn6Rc1Ys5Qe2Jv
Nice to have
• Cool design: https://layoutmarket.example/item/business-solution-brochure-template/46182057?s_rank=3
• Cool design 2: https://layoutmarket.example/item/travel-agency-catalog-brochure/47269815?s_rank=6
Should not have
• Do not change the dimensions. You have the design attached, indd file. Needs work and update.

```html
<!DOCTYPE html>
<html lang="en">
<head>
<meta charset="utf-8">
<title>Selvo Trips Croatia – Company Profile</title>
<link rel="stylesheet" href="https://fonts.googleapis.com/css2?family=Oswald:wght@300;400;500;700&family=Playfair+Display:ital,wght@1,400&family=Source+Serif+4:wght@400&display=swap">
<style>
:root{
  --white:#ffffff;
  --ink:#2b3440;
  --agent-photo-a:#dfe6ee;
  --agent-photo-b:#c7b9a8;
  --agent-veil:rgba(96,140,196,.62);
  --music-photo-a:#8fa39c;
  --music-photo-b:#d9dde0;
  --sea-a:#2f6fb8;
  --sea-b:#4ea4d8;
  --cliff:#c9a77a;
  --icon-col:#93c2ea;
  --info-col:#a2cbee;
  --weather-col:#aed3f2;
  --crowds-col:#c4dff6;
  --prices-col:#b8d7f3;
  --bar-low:#e8f3fc;
  --bar-high:#3f86cc;
  --logo-box:rgba(200,222,245,.45);
}
*{box-sizing:border-box;margin:0;padding:0}
html,body{width:1200px;height:240px;overflow:hidden;background:var(--white)}
.brochure{position:relative;width:1200px;height:240px;font-family:"Oswald",sans-serif;color:var(--white)}
.panel{position:absolute;top:0;height:240px;overflow:hidden}

/* Panel: travel agents */
.agents{left:0;width:240px}
.agents .photo{position:absolute;inset:0;background:linear-gradient(100deg,var(--agent-photo-a) 0%,#eef1f4 55%,var(--agent-photo-b) 100%)}
.agents .veil{position:absolute;left:0;top:0;width:115px;height:240px;background:var(--agent-veil)}
.agents .title{position:absolute;left:14px;top:68px;width:200px}
.agents h2{font-weight:500;font-size:12px;letter-spacing:.3px;line-height:1.1}
.agents .sub{font-family:"Playfair Display",serif;font-style:italic;font-size:12px;line-height:1.2}
.agents ul{position:absolute;left:14px;top:102px;width:96px;list-style:none;font-family:"Source Serif 4",serif;font-size:4.2px;line-height:1.4}
.agents li{position:relative;padding-left:6px;margin-bottom:5px}
.agents li::before{content:"";position:absolute;left:0;top:2px;width:2.5px;height:2.5px;border-radius:50%;background:var(--white)}

/* Panel: contact */
.contact{left:240px;width:240px}
.contact .photo{position:absolute;inset:0;background:linear-gradient(160deg,var(--music-photo-a) 0%,var(--music-photo-b) 60%,#b7a998 100%)}
.contact .frame{position:absolute;left:20px;top:-1px;width:218px;height:225px;border:1px solid rgba(43,52,64,.55)}
.brand{display:flex;align-items:center;gap:5px;font-weight:700;color:var(--white);letter-spacing:1px;line-height:1}
.brand .dot{width:7px;height:7px;border-radius:50%;background:var(--white)}
.contact .brand{position:absolute;left:92px;top:126px;font-size:15px}
.contact h3{position:absolute;left:85px;top:163px;font-weight:400;font-size:11px;letter-spacing:.3px;line-height:1.2}
.contact address{position:absolute;left:85px;top:182px;font-style:normal;font-family:"Source Serif 4",serif;font-size:4.6px;line-height:1.55}

/* Panel: when to travel */
.facts{left:480px;width:358px;display:flex}
.col{height:240px;position:relative}
.col-icons{width:32px;background:var(--icon-col)}
.col-info{width:66px;background:var(--info-col)}
.col-weather{width:50px;background:var(--weather-col)}
.col-crowds{width:108px;background:var(--crowds-col)}
.col-prices{width:102px;background:var(--prices-col)}
.col-head{position:absolute;top:12px;left:0;right:0;text-align:center;font-size:6.5px;font-weight:400;letter-spacing:.2px;line-height:1}
.icon{position:absolute;left:7px;width:18px;height:18px}
.fact{position:absolute;left:2px;right:2px;text-align:center;font-size:6px;line-height:1.45;text-transform:uppercase}
.months{position:absolute;top:26px;left:0;right:0;display:flex;flex-direction:column;align-items:center}
.month{height:16px;display:flex;flex-direction:column;align-items:center;font-size:4.8px;line-height:1}
.month svg{width:11px;height:8px;margin-top:1px}
.rows{position:absolute;top:26px;left:10px;right:10px}
.row{height:16px;display:flex;align-items:center}
.crowd-bar{height:6px;border-radius:3px;background:linear-gradient(90deg,var(--bar-low),var(--bar-high))}
.price{font-size:6px;letter-spacing:1.5px;line-height:1;width:100%;text-align:center}
.price .off{opacity:.4}

/* Blank inside panel */
.blank{left:838px;width:120px;background:var(--white)}

/* Cover */
.cover{left:958px;width:242px}
.cover .photo{position:absolute;inset:0;background:linear-gradient(90deg,var(--sea-a) 0%,var(--sea-b) 55%,var(--cliff) 100%)}
.cover .logo-window{position:absolute;left:52px;top:0;width:140px;height:116px;background:var(--logo-box);display:flex;align-items:center;justify-content:center}
.cover .brand{font-size:17px}
.cover .kicker{position:absolute;left:0;right:0;top:166px;text-align:center;font-weight:400;font-size:8px;letter-spacing:3px;line-height:1}
.cover h1{position:absolute;left:0;right:0;top:178px;text-align:center;font-weight:700;font-size:27px;letter-spacing:.5px;line-height:1}
.cover .tagline{position:absolute;left:0;right:0;top:209px;text-align:center;font-family:"Playfair Display",serif;font-style:italic;font-size:15px;line-height:1}
</style>
</head>
<body>
<svg width="0" height="0" style="position:absolute">
  <symbol id="cloud" viewBox="0 0 18 12"><path d="M4 11h10a3 3 0 0 0 0-6 4.5 4.5 0 0 0-8.5-1A3.5 3.5 0 0 0 4 11z" fill="none" stroke="#fff" stroke-width="1.2"/></symbol>
  <symbol id="sun" viewBox="0 0 18 12"><circle cx="9" cy="6" r="2.6" fill="none" stroke="#fff" stroke-width="1.2"/><path d="M9 0v1.6M9 10.4V12M3 6h1.6M13.4 6H15M4.8 1.8l1.1 1.1M12.1 9.1l1.1 1.1M4.8 10.2l1.1-1.1M12.1 2.9l1.1-1.1" stroke="#fff" stroke-width="1"/></symbol>
</svg>

<main class="brochure">

  <section class="panel agents">
    <div class="photo" role="img" aria-label="Photo of a smiling travel consultant wearing a headset at her desk"></div>
    <div class="veil"></div>
    <div class="title">
      <h2>TRAVEL AGENTS,</h2>
      <p class="sub">what's in it for YOU?</p>
    </div>
    <ul>
      <li>We work exclusively with travel agents, we don't market or sell directly to the public.</li>
      <li>High paying commission up to 15%</li>
      <li>Incentive programs available</li>
      <li>Travel agent support and fam trips</li>
      <li>We are your strongest local link in Croatia and Eastern Europe!</li>
    </ul>
  </section>

  <section class="panel contact">
    <div class="photo" role="img" aria-label="Photo of folk musicians in traditional costume playing string instruments outdoors"></div>
    <div class="frame"></div>
    <div class="brand"><span class="dot"></span>SELVO TRIPS</div>
    <h3>SELVO TRIPS CROATIA</h3>
    <address>
      418 Alder Lane, Brookfield, OH, 45990<br>
      Tollfree +1 800 555 0142<br>
      Direct +1 555 010 4477<br>
      sales@selvotrips.example<br>
      web: www.selvotrips.example
    </address>
  </section>

  <section class="panel facts">
    <div class="col col-icons">
      <svg class="icon" style="top:11px" viewBox="0 0 18 18"><path d="M9 2c4.4 0 7.5 2.7 7.5 6s-3.1 6-7.5 6c-1 0-2-.1-2.8-.4L3 15.5l.9-3C2.7 11.4 1.5 9.9 1.5 8c0-3.3 3.1-6 7.5-6z" fill="none" stroke="#fff" stroke-width="1.1"/><circle cx="6" cy="8" r=".8" fill="#fff"/><circle cx="9" cy="8" r=".8" fill="#fff"/><circle cx="12" cy="8" r=".8" fill="#fff"/></svg>
      <svg class="icon" style="top:45px" viewBox="0 0 18 18"><rect x="1.5" y="4" width="15" height="10" fill="none" stroke="#fff" stroke-width="1.1"/><text x="9" y="12.2" text-anchor="middle" font-size="8" fill="#fff" font-family="Oswald,sans-serif">$</text></svg>
      <svg class="icon" style="top:77px" viewBox="0 0 18 18"><path d="M2 4h14v12H2z" fill="none" stroke="#fff" stroke-width="1.1"/><path d="M9 5.5a3 3 0 0 1 3 3c0 2.2-3 5-3 5s-3-2.8-3-5a3 3 0 0 1 3-3z" fill="none" stroke="#fff" stroke-width="1.1"/></svg>
      <svg class="icon" style="top:111px" viewBox="0 0 18 18"><path d="M9 1v4M7.5 2.5h3M4 17V9l5-4 5 4v8zM7.5 17v-4h3v4" fill="none" stroke="#fff" stroke-width="1.1"/></svg>
      <svg class="icon" style="top:141px" viewBox="0 0 18 18"><circle cx="5" cy="6" r="3.2" fill="none" stroke="#fff" stroke-width="1.1"/><circle cx="12.5" cy="7" r="3.6" fill="none" stroke="#fff" stroke-width="1.1"/><path d="M5 9.2V16M12.5 10.6V16M2 16h14" stroke="#fff" stroke-width="1.1"/></svg>
      <svg class="icon" style="top:173px" viewBox="0 0 18 18"><circle cx="6" cy="4" r="2" fill="none" stroke="#fff" stroke-width="1.1"/><circle cx="12" cy="4" r="2" fill="none" stroke="#fff" stroke-width="1.1"/><path d="M3.5 16V8.5h5V16M9.5 16V8.5h5V16" fill="none" stroke="#fff" stroke-width="1.1"/></svg>
      <svg class="icon" style="top:207px" viewBox="0 0 18 18"><path d="M1 11l15-4c1 0 1.5 1 .5 1.5L6 13H2zM6 8.5 4 6h2l3 1.5" fill="none" stroke="#fff" stroke-width="1.1"/></svg>
    </div>
    <div class="col col-info">
      <p class="fact" style="top:12px">Croatian</p>
      <p class="fact" style="top:43px">Kuna (HRK)</p>
      <p class="fact" style="top:73px">UNESCO: 8 properties from the world heritage list</p>
      <p class="fact" style="top:116px">Catholic</p>
      <p class="fact" style="top:143px">8 spectacular national parks</p>
      <p class="fact" style="top:177px">Population:<br>4.284 million</p>
      <p class="fact" style="top:209px">Airports: Zagreb, Pula, Zadar, Split, Dubrovnik</p>
    </div>
    <div class="col col-weather">
      <p class="col-head">WEATHER</p>
      <div class="months">
        <div class="month">JAN<svg><use href="#cloud"/></svg></div>
        <div class="month">FEB<svg><use href="#cloud"/></svg></div>
        <div class="month">MAR<svg><use href="#cloud"/></svg></div>
        <div class="month">APR<svg><use href="#cloud"/></svg></div>
        <div class="month">MAY<svg><use href="#cloud"/></svg></div>
        <div class="month">JUN<svg><use href="#sun"/></svg></div>
        <div class="month">JUL<svg><use href="#sun"/></svg></div>
        <div class="month">AUG<svg><use href="#sun"/></svg></div>
        <div class="month">SEP<svg><use href="#sun"/></svg></div>
        <div class="month">OCT<svg><use href="#sun"/></svg></div>
        <div class="month">NOV<svg><use href="#cloud"/></svg></div>
        <div class="month">DEC<svg><use href="#cloud"/></svg></div>
      </div>
    </div>
    <div class="col col-crowds">
      <p class="col-head">CROWDS</p>
      <div class="rows">
        <div class="row"><span class="crowd-bar" style="width:12%"></span></div>
        <div class="row"><span class="crowd-bar" style="width:12%"></span></div>
        <div class="row"><span class="crowd-bar" style="width:22%"></span></div>
        <div class="row"><span class="crowd-bar" style="width:35%"></span></div>
        <div class="row"><span class="crowd-bar" style="width:48%"></span></div>
        <div class="row"><span class="crowd-bar" style="width:72%"></span></div>
        <div class="row"><span class="crowd-bar" style="width:92%"></span></div>
        <div class="row"><span class="crowd-bar" style="width:100%"></span></div>
        <div class="row"><span class="crowd-bar" style="width:62%"></span></div>
        <div class="row"><span class="crowd-bar" style="width:34%"></span></div>
        <div class="row"><span class="crowd-bar" style="width:14%"></span></div>
        <div class="row"><span class="crowd-bar" style="width:20%"></span></div>
      </div>
    </div>
    <div class="col col-prices">
      <p class="col-head">PRICES</p>
      <div class="rows">
        <div class="row"><p class="price">$<span class="off">$$$</span></p></div>
        <div class="row"><p class="price">$<span class="off">$$$</span></p></div>
        <div class="row"><p class="price">$<span class="off">$$$</span></p></div>
        <div class="row"><p class="price">$$<span class="off">$$</span></p></div>
        <div class="row"><p class="price">$$<span class="off">$$</span></p></div>
        <div class="row"><p class="price">$$$<span class="off">$</span></p></div>
        <div class="row"><p class="price">$$$$</p></div>
        <div class="row"><p class="price">$$$$</p></div>
        <div class="row"><p class="price">$$$<span class="off">$</span></p></div>
        <div class="row"><p class="price">$$<span class="off">$$</span></p></div>
        <div class="row"><p class="price">$<span class="off">$$$</span></p></div>
        <div class="row"><p class="price">$$<span class="off">$$</span></p></div>
      </div>
    </div>
  </section>

  <section class="panel blank"></section>

  <section class="panel cover">
    <div class="photo" role="img" aria-label="Photo of a wooden sailing ship anchored in turquoise water beside sunlit limestone cliffs"></div>
    <div class="logo-window"><div class="brand"><span class="dot"></span>SELVO TRIPS</div></div>
    <p class="kicker">COMPANY PROFILE</p>
    <h1>CROATIA.</h1>
    <p class="tagline">We live it. You'll love it.</p>
  </section>

</main>
</body>
</html>
```